依頼詳細
レスポンシブウェブデザインを意識したデザインでお願いします。

デザインに関しては、添付してあるデザインレイアウトシートを基にお願いします。
参考サイトのURLはデザインレイアウトシートに記載してあります。
色合いはグリーンかブルーを基調にお願いします。
新規のウェブサイトですので、既存サイトはありません。
ロゴも不要です。(後ではめ込むので社名だけテキストでレイアウトをお願いします。)
また、写真データも添付するので、レイアウトシートのイメージ画像に当て込んでください。

まずはパソコンサイトのデザインをお願いします。
当選後、スマホデザインをお願いします。

既存のテンプレートを使う場合は
テンプレート名を下記のような記載を提案の中にいれてください。
例:WordpressテーマはCorpLumen、デザインスキンは無料のQRN2019 LX4(http://corplumen.example/ex_plugin/qrnfuji2019_lx4/)をベースにデザインいたしました。
など

写真データで足りない場合は、一旦他のサイトや参考URLの写真をサンプルとして入れてください。(サンプルなどの表記をお願いします)
また、購入が必要な写真などを利用した場合は、Pixora Stock(https://stock.pixora-img.example/jp/)からファイル番号と価格を教えてください。
ページ数
1ページ
希望イメージ
シンプル 複雑
単色 カラフル
暗い 明るい
日常 高級
遊び心 厳粛
未来的 伝統的
女性的 男性的
希望する色
青系、緑系
納品ファイル
• イラストレーター形式 (.ai)
• フォトショップ形式 (.psd)
• PNG形式 (.png)
補足説明
上記のいずれか1つ。アウトラインありとなしの2つ。

こちらの要望を汲んで、デザインしていただきました。
ありがとうございました。

たくさんのご提案ありがとうございました。
次回もぜひ、よろしくお願い致します。

```html
<!DOCTYPE html>
<html lang="ja">
<head>
<meta charset="utf-8">
<title>有限会社緑翔</title>
<link rel="stylesheet" href="https://fonts.googleapis.com/css2?family=Noto+Sans+JP:wght@400;500;700&family=Noto+Serif+JP:wght@400;600;700&display=swap">
<style>
:root{
  --green:#4e8a34;
  --green-dark:#2f5e1f;
  --green-light:#6fa84d;
  --ink:#222;
  --text:#555;
  --muted:#999;
  --gray-bg:#f2f2f2;
  --line:#ddd;
  --white:#fff;
}
*{box-sizing:border-box;margin:0;padding:0}
html,body{width:1200px;height:4412px;overflow:hidden}
body{font-family:"Noto Sans JP",sans-serif;color:var(--text);background:var(--white);position:relative}
.site-header{position:absolute;top:0;left:0;width:1200px;height:96px;background:rgba(255,255,255,.95);display:flex;align-items:center;justify-content:space-between;padding:0 40px 0 28px;z-index:2}
.site-name{font-family:"Noto Serif JP",serif;font-weight:700;font-size:38px;color:var(--ink);letter-spacing:2px}
.global-nav{display:flex}
.global-nav a{font-size:15px;color:var(--green);text-decoration:none;padding:0 20px;border-left:1px solid var(--line);white-space:nowrap}
.global-nav a:first-child{border-left:none}
.hero{position:absolute;top:0;left:0;width:1200px;height:840px;background:linear-gradient(180deg,#5e9ad8 0%,#9fc6ec 35%,#d8dfe4 60%,#b49a6c 85%,#8b7450 100%)}
.hero-title{position:absolute;left:100px;top:415px;font-size:58px;font-weight:700;color:var(--ink);letter-spacing:4px;text-shadow:0 0 10px #fff,0 0 18px #fff;white-space:nowrap}
.hero-btn{position:absolute;right:0;top:782px;width:220px;height:46px;background:var(--green);color:#fff;font-size:15px;display:flex;align-items:center;justify-content:center;gap:14px}
.section-head{position:relative;height:100px;width:1100px;white-space:nowrap}
.section-head .en{position:absolute;left:0;bottom:12px;font-family:"Noto Serif JP",serif;font-weight:400;font-size:48px;color:var(--green);z-index:1;white-space:nowrap;line-height:1.2}
.section-head .ja{position:absolute;bottom:0;font-family:"Noto Serif JP",serif;font-size:90px;color:rgba(0,0,0,.07);letter-spacing:8px;line-height:1;white-space:nowrap}
.feature .ja{left:244px}
.business .ja{left:372px}
.career .ja{left:452px}
.news .ja{left:112px}
.btn{display:inline-flex;align-items:center;justify-content:center;font-size:14px;text-decoration:none;white-space:nowrap}
.btn-green{background:var(--green);color:#fff}
.btn-outline{border:1px solid #888;color:var(--text);background:#fff;border-radius:4px}
.feature{position:absolute;top:840px;left:0;width:1200px;height:540px;background:var(--gray-bg)}
.feature .section-head{position:absolute;left:48px;top:90px}
.feature-text{position:absolute;left:48px;top:230px;width:500px;font-size:15px;line-height:2}
.feature .btn{position:absolute;left:160px;top:390px;width:210px;height:50px}
.feature-photo{position:absolute;left:600px;top:100px;width:560px;height:340px;background:linear-gradient(135deg,#7d8a8c,#c8cfcf 45%,#5a6866)}
.business{position:absolute;top:1380px;left:0;width:1200px;height:1000px}
.business .section-head{position:absolute;left:48px;top:40px}
.card{position:absolute;width:300px;height:360px}
.card-photo{height:160px;position:relative;display:flex;align-items:flex-end;justify-content:center;padding-bottom:10px}
.card-label{font-family:"Noto Serif JP",serif;font-size:20px;color:#fff;font-weight:600;text-shadow:0 0 6px #000;white-space:nowrap}
.card-text{font-size:12px;line-height:1.9;margin:14px 4px 0;height:92px}
.card .btn{display:flex;width:200px;height:40px;margin:12px auto 0}
.career{position:absolute;top:2388px;left:0;width:1200px;height:372px;background:linear-gradient(180deg,#f3f3f3 0%,#e3e3e3 50%,#b9a57c 80%,#8e7850 100%)}
.career .section-head{position:absolute;left:48px;top:20px}
.career-text{position:absolute;left:72px;top:150px;width:820px;font-size:14px;line-height:2.1;color:var(--muted)}
.career .btn{position:absolute;left:940px;top:196px;width:180px;height:44px}
.news{position:absolute;top:2800px;left:0;width:1200px;height:720px;background:var(--gray-bg)}
.news .section-head{position:absolute;left:48px;top:36px}
.news-list{position:absolute;left:100px;top:190px;width:1050px;list-style:none}
.news-list li{display:flex;align-items:center;height:80px;border-bottom:1px solid var(--line);font-size:14px}
.news-date{width:90px;color:var(--text)}
.news-tag{width:80px;height:22px;border:1px solid;border-radius:3px;font-size:11px;display:flex;align-items:center;justify-content:center;margin-right:20px}
.tag-info{color:var(--green);border-color:var(--green)}
.tag-recruit{color:#d98a3a;border-color:#d98a3a}
.news-title{color:var(--ink);white-space:nowrap}
.news .btn{position:absolute;left:515px;top:600px;width:170px;height:40px}
.contact-band{position:absolute;top:3580px;left:0;width:1200px;height:130px;background:var(--green);color:#fff;display:flex;align-items:center;padding:0 50px}
.contact-label{font-size:15px;margin-right:40px;white-space:nowrap}
.contact-tel{font-size:40px;font-weight:500;letter-spacing:2px;line-height:1;white-space:nowrap}
.contact-hours{font-size:11px;margin-top:6px}
.contact-divider{width:1px;height:70px;background:rgba(255,255,255,.5);margin:0 40px}
.contact-msg{font-size:15px;margin-right:60px;white-space:nowrap}
.contact-band .btn{width:220px;height:48px;background:#fff;color:var(--green);border-radius:3px}
.site-footer{position:absolute;top:3800px;left:0;width:1200px;height:560px;background:var(--gray-bg)}
.footer-nav{position:absolute;left:200px;top:30px;display:flex;gap:60px}
.footer-nav h4{font-size:14px;color:var(--ink);margin-bottom:8px;white-space:nowrap}
.footer-nav li{list-style:none;font-size:12px;color:var(--muted);line-height:1.9}
.footer-name{position:absolute;left:0;width:1200px;top:190px;text-align:center;font-family:"Noto Serif JP",serif;font-weight:700;font-size:78px;color:var(--ink);letter-spacing:6px}
.footer-info{position:absolute;left:360px;top:340px;font-size:16px;color:var(--ink);border-collapse:collapse}
.footer-info th{text-align:left;font-weight:500;width:110px;padding:8px 0;white-space:nowrap}
.footer-info td{padding:8px 0;white-space:nowrap}
.copyright{position:absolute;top:4360px;left:0;width:1200px;height:52px;background:var(--green-dark);color:#fff;font-size:13px;display:flex;align-items:center;justify-content:center}
</style>
</head>
<body>

<header class="site-header">
  <div class="site-name">有限会社緑翔</div>
  <nav class="global-nav">
    <a href="#">ホーム</a><a href="#">会社案内</a><a href="#">会社紹介</a><a href="#">事業内容</a><a href="#">採用情報</a><a href="#">お問い合わせ</a>
  </nav>
</header>

<section class="hero" role="img" aria-label="青空を背景に足場が組まれた建設中の建物の写真">
  <h1 class="hero-title">足場の新しい未来をつくる</h1>
  <a class="hero-btn">会社の特徴 <span>›</span></a>
</section>

<section class="feature">
  <div class="section-head"><span class="ja">特徴</span><h2 class="en">The feature</h2></div>
  <p class="feature-text">当社の特徴に関するテキストが入ります。仮設資材の管理から施工まで一貫して対応し、安全で効率的な足場をお届けします。地域に根ざした確かな技術で現場を支えます。</p>
  <a class="btn btn-green">詳しくはこちら</a>
  <div class="feature-photo" role="img" aria-label="仮設資材が並ぶ倉庫内部の写真"></div>
</section>

<section class="business">
  <div class="section-head"><span class="ja">業務内容</span><h2 class="en">Business content</h2></div>

  <article class="card" style="left:100px;top:220px">
    <div class="card-photo" role="img" aria-label="仮設資材の写真" style="background:linear-gradient(135deg,#8fa4b8,#d3dde6)"><span class="card-label">建設用仮設資材</span></div>
    <p class="card-text">建設現場で使用する仮設資材の販売とレンタルを行っています。品質管理を徹底した資材をご用意します。</p>
    <a class="btn btn-outline">詳しく見る</a>
  </article>
  <article class="card" style="left:450px;top:220px">
    <div class="card-photo" role="img" aria-label="住宅用足場の写真" style="background:linear-gradient(135deg,#6d9fd0,#c6d7c8)"><span class="card-label">住宅用足場工事</span></div>
    <p class="card-text">戸建住宅の新築や改修に合わせた足場を設計し、安全第一で迅速に組立と解体を行います。</p>
    <a class="btn btn-outline">詳しく見る</a>
  </article>
  <article class="card" style="left:800px;top:220px">
    <div class="card-photo" role="img" aria-label="鋼製足場板の写真" style="background:linear-gradient(135deg,#6e8aa6,#a9b7c2)"><span class="card-label">鋼製足場板</span></div>
    <p class="card-text">耐久性に優れた鋼製足場板を取り扱っています。現場の規模に応じて必要な数量をご提供します。</p>
    <a class="btn btn-outline">詳しく見る</a>
  </article>
  <article class="card" style="left:100px;top:600px">
    <div class="card-photo" role="img" aria-label="ユニットハウスの写真" style="background:linear-gradient(135deg,#8c8f86,#c9c7bd)"><span class="card-label">高機能ユニットハウス</span></div>
    <p class="card-text">現場事務所や休憩所として使える快適なユニットハウスを短期から長期までお貸しします。</p>
    <a class="btn btn-outline">詳しく見る</a>
  </article>
  <article class="card" style="left:450px;top:600px">
    <div class="card-photo" role="img" aria-label="太陽光パネルの写真" style="background:linear-gradient(135deg,#4f6f8f,#a7c0d6)"><span class="card-label">太陽光発電</span></div>
    <p class="card-text">太陽光発電設備の設置に必要な架台や施工をご提案し、再生可能エネルギーの普及に貢献します。</p>
    <a class="btn btn-outline">詳しく見る</a>
  </article>
  <article class="card" style="left:800px;top:600px">
    <div class="card-photo" role="img" aria-label="資材整備作業の写真" style="background:linear-gradient(135deg,#5f6d74,#b3b8b2)"><span class="card-label">資材整備メンテ</span></div>
    <p class="card-text">使用後の資材を点検し、洗浄や補修を行って次の現場でも安心して使える状態に整えます。</p>
    <a class="btn btn-outline">詳しく見る</a>
  </article>
</section>

<section class="career" role="img" aria-label="働く人々のシルエットの写真">
  <div class="section-head"><span class="ja">採用情報</span><h2 class="en">Career opportunities</h2></div>
  <p class="career-text">採用情報のテキストが入ります。足場の施工や資材管理に携わる仲間を募集しています。未経験の方も丁寧に指導しますので安心してご応募ください。経験者の方は待遇面で優遇いたします。一緒に現場の未来をつくりましょう。</p>
  <a class="btn btn-outline">詳しく見る</a>
</section>

<section class="news">
  <div class="section-head"><span class="ja">最新情報</span><h2 class="en">News</h2></div>
  <ul class="news-list">
    <li><span class="news-date">2019.00.00</span><span class="news-tag tag-info">お知らせ</span><span class="news-title">ホームページを公開しました。今後とも当社をよろしくお願いいたします。</span></li>
    <li><span class="news-date">2019.00.00</span><span class="news-tag tag-recruit">採用情報</span><span class="news-title">現場スタッフの募集を開始しました。詳しくは採用情報ページをご覧ください。</span></li>
    <li><span class="news-date">2019.00.00</span><span class="news-tag tag-recruit">採用情報</span><span class="news-title">事務スタッフの募集を開始しました。ご応募を心よりお待ちしております。</span></li>
    <li><span class="news-date">2019.00.00</span><span class="news-tag tag-info">お知らせ</span><span class="news-title">年末年始の休業期間についてお知らせいたします。ご了承ください。</span></li>
    <li><span class="news-date">2019.00.00</span><span class="news-tag tag-info">お知らせ</span><span class="news-title">新しいユニットハウスの取り扱いを開始しました。お気軽にご相談ください。</span></li>
  </ul>
  <a class="btn btn-outline">一覧を見る</a>
</section>

<section class="contact-band">
  <span class="contact-label">お電話でのお問い合わせ</span>
  <div>
    <div class="contact-tel">0250-00-4812</div>
    <div class="contact-hours">受付時間 平日 9:00〜17:00</div>
  </div>
  <span class="contact-divider"></span>
  <span class="contact-msg">お気軽にご相談ください</span>
  <a class="btn">メールからのお問い合わせ</a>
</section>

<footer class="site-footer">
  <nav class="footer-nav">
    <div><h4>ホーム</h4></div>
    <div><h4>お知らせ</h4><ul><li>サブページ</li><li>サブページ</li><li>サブページ</li></ul></div>
    <div><h4>会社概要</h4><ul><li>サブページ</li><li>サブページ</li><li>サブページ</li></ul></div>
    <div><h4>事業内容</h4><ul><li>サブページ</li><li>サブページ</li><li>サブページ</li></ul></div>
    <div><h4>採用情報</h4><ul><li>サブページ</li><li>サブページ</li></ul></div>
    <div><h4>お問い合わせ</h4><ul><li>サブページ</li></ul></div>
  </nav>
  <div class="footer-name">有限会社緑翔</div>
  <table class="footer-info">
    <tr><th>住　所</th><td>〒900-0000　架空県 緑野市若葉町1番2号</td></tr>
    <tr><th>電話番号</th><td>025-000-7315</td></tr>
    <tr><th>事業内容</th><td>建築、住宅用足場 足場</td></tr>
  </table>
</footer>

<div class="copyright">Copyright © デザイン事務 サンプル企画 All rights reserved.</div>

</body>
</html>
```